Projektbeschreibung:
Wir benötigen ein ansprechendes A4-Flyer-Design für die Neueröffnung von "Hanni’s ZehenGlanz", einem professionellen Fußpflege-Studio in Bad Lindenau. Der Flyer soll das Studio und seine Leistungen vorstellen und einen exklusiven Eröffnungsgutschein enthalten. Der Gutschein befindet sich im unteren Bereich des Flyers und muss durch eine deutlich sichtbare Schnittlinie abtrennbar gestaltet werden, sodass Kunden ihn einfach herausschneiden können. Zusätzlich wird ein passendes Logo für "Hanni’s ZehenGlanz" benötigt.

Designanforderungen:
Flyer Format: A4, Hochformat.

Sprache:
Deutsch

Struktur:
Flyer-Text im oberen Bereich, Gutscheinbereich im unteren Drittel.

Schnittlinie: Gestalten Sie eine deutlich sichtbare, gestrichelte Linie zwischen dem Flyertext und dem Gutscheinbereich mit einer kleinen Scherensymbol-Darstellung am Rand, um klar zu zeigen, dass dieser Bereich abgeschnitten werden kann.

Gestaltungsstil:
Einladend, professionell und passend zu einem Fußpflege-Studio. Die Farben sollten sanft und beruhigend wirken: vorwiegend Türkis und Weiß, eventuell kombiniert mit Rosa.

Textgestaltung:
Die folgenden Texte müssen in den jeweiligen Bereichen des Flyers und des Gutscheins integriert und klar strukturiert dargestellt werden:

Flyer Text:
Hannis ZehenGlanz lädt Sie herzlich zur Neueröffnung ein!
Ihr neues Fußpflege-Studio in Bad Lindenau.

Liebe Kundinnen und Kunden,
es ist endlich soweit: Mit viel Liebe und Leidenschaft öffnen wir die Türen zu unserem brandneuen Hannis ZehenGlanz in der Lindwurmgasse 47, 8477 Bad Lindenau!
Tauchen Sie ein in eine Welt, in der Ihre Füße verwöhnt und verschönert werden – ein Ort, an dem Entspannung und Pflege Hand in Hand gehen. Egal, ob Sie intensive Regeneration oder einen frischen Look für Ihre Füße wünschen – bei uns stehen Sie im Mittelpunkt!

Warum zu uns?
Bei Hannis ZehenGlanz erwarten Sie wohltuende Behandlungen, die Sie nicht nur äußerlich strahlen lassen, sondern Ihnen auch ein tiefes Wohlgefühl schenken.
Wir gehen individuell auf Ihre Bedürfnisse ein und gestalten jeden Besuch zu einem besonderen Erlebnis, das Ihnen ein Lächeln ins Gesicht zaubert.

Terminvereinbarung
Unser Studio arbeitet mit einem Terminbetrieb, um Ihnen die bestmögliche Betreuung zu gewährleisten. Termine sind ausschließlich nach Vereinbarung möglich.
Ich freue mich sehr darauf, Ihre Reservierungen ab dem 15.10.2024 telefonisch unter 0664/38291647 entgegenzunehmen. Rufen Sie uns an und sichern Sie sich Ihren Wunschtermin!
Besuchen Sie uns in unserem gemütlichen und barrierefreien Ambiente und lassen Sie sich von unserer Expertise begeistern. Ihre Füße werden es Ihnen danken!
Ich freue mich schon sehr darauf, Sie persönlich bei Hannis ZehenGlanz begrüßen zu dürfen!
Herzlichst, Ihre Milena Tarkov

Gutschein Text:
Exklusiver Eröffnungsgutschein*
Zur Feier unserer Neueröffnung möchten wir Ihnen etwas Besonderes schenken:
Profitieren Sie von 30 % Rabatt auf alle unsere Behandlungen – ein Geschenk für Sie und Ihre Füße!
*Dieser Gutschein ist gültig bis zum 31.12.2024 und einmalig einlösbar. Bitte beachten Sie, dass er nicht mit anderen Aktionen kombinierbar ist.

Gutscheinbereich: Der Gutschein soll optisch hervorstechen, z.B. durch Farbunterschiede, Rahmen oder Symbole. Der Text „Exklusiver Eröffnungsgutschein“ muss deutlich sichtbar sein und das Design soll den Eindruck eines wertvollen, einmaligen Angebots vermitteln.

Logo & Branding:
Das Logo soll passend zu einem Fußpflege-Studio gestaltet werden und sanfte, beruhigende Farben wie Türkis, Weiß und Rosa integrieren. Es sollte eine Mischung aus Schriftzug („Hanni’s ZehenGlanz“) und einem passenden Symbol oder grafischem Element enthalten, das die Thematik der Fußpflege widerspiegelt.

Bilder & Elemente:
Optional können dezente Fußpflege-Bilder, Symbole (z.B. entspannende Füße, usw.) und weitere Elemente integriert werden, um das Design visuell zu unterstützen.

Ziel:
Der Flyer soll Kunden auf die Neueröffnung aufmerksam machen, Vertrauen aufbauen und den Gutschein als attraktives Angebot hervorheben. Die deutlich sichtbare Schnittlinie sorgt dafür, dass der Gutscheinbereich leicht abgetrennt und aufbewahrt werden kann.

```html
<!DOCTYPE html>
<html lang="de">
<head>
<meta charset="utf-8">
<title>Hanni’s ZehenGlanz – Neueröffnung</title>
<link href="https://fonts.googleapis.com/css2?family=Italiana&family=Josefin+Sans:wght@300;400&family=Poppins:ital,wght@0,400;0,500;0,600;0,700;1,400;1,500&family=Cinzel:wght@400&display=swap" rel="stylesheet">
<style>
  :root{
    --stage:#b5b5b5;
    --paper:#ffffff;
    --pink:#ea90ba;
    --pink-band:#f3a9ca;
    --teal:#4dbfbf;
    --teal-deep:#2aa9aa;
    --teal-light:#79dcdc;
    --ink:#1f1f1f;
    --ink-teal:#0f3b3b;
  }
  *{margin:0;padding:0;box-sizing:border-box}
  html,body{width:1200px;height:1008px;overflow:hidden;background:var(--stage)}
  .flyer{position:absolute;left:260px;top:23px;width:680px;height:962px;background:var(--paper);overflow:hidden;font-family:"Poppins",sans-serif;color:var(--ink)}
  .abs{position:absolute}
  .floral-bg{left:0;top:0;width:680px;height:260px;background:linear-gradient(180deg,#efefef 0%,rgba(255,255,255,0) 100%)}
  .title{left:44px;top:28px;font-family:"Italiana",serif;font-size:72px;line-height:1;color:var(--pink)}
  .subtitle{left:46px;top:110px;font-family:"Josefin Sans",sans-serif;font-weight:300;font-size:38px;line-height:1;color:var(--teal);letter-spacing:-.5px}
  .invite{left:47px;top:156px;font-weight:600;font-size:15.5px;line-height:20px;color:#2b2b2b}
  .location{left:46px;top:205px;display:flex;align-items:center;gap:6px;font-family:"Cinzel",serif;font-size:22px;color:var(--pink)}
  .brand-mark{left:486px;top:66px;display:flex;align-items:center;gap:6px;font-weight:500;font-size:17px;color:var(--pink)}
  .brand-mark i{width:10px;height:10px;border-radius:50%;background:var(--teal)}
  .intro{left:47px;top:247px;width:365px;font-size:9.6px;line-height:12.4px}
  .intro .greet{color:var(--teal-deep);font-weight:600;font-size:10.5px}
  .intro .lead{font-weight:600}
  .band{left:0;top:357px}
  .why{left:47px;top:393px;width:430px}
  .why h2{font-weight:700;font-size:18px;color:#fff;letter-spacing:.3px;margin-bottom:3px}
  .why p{font-size:9.8px;line-height:12.6px;color:#2a1a22}
  .feet-photo{left:325px;top:525px;width:290px;height:185px;background:radial-gradient(ellipse 50% 40% at 55% 62%,#efcfbf 0%,#f6e6dd 55%,rgba(255,255,255,0) 100%)}
  .legs-photo{left:448px;top:249px}
  .quote{left:412px;top:282px;font-family:"Italiana",serif;font-size:140px;line-height:1;color:transparent;-webkit-text-stroke:1.4px var(--pink)}
  .booking{left:47px;top:536px;width:380px}
  .booking h2{font-weight:600;font-size:22px;color:var(--teal-deep);margin-bottom:4px}
  .booking .claim{font-weight:700;font-size:12.3px;line-height:14px;color:var(--ink-teal);margin-bottom:9px}
  .booking .note{font-size:10.5px;line-height:12.8px;margin-bottom:10px}
  .booking .date{font-weight:600;font-size:12.8px;line-height:15px}
  .booking .date .pink{color:var(--pink);font-weight:500}
  .booking .date .phone{color:var(--teal-deep);font-weight:600;display:inline-flex;align-items:center;gap:2px}
  .booking .sign{margin-top:13px;font-style:italic;font-size:7.4px;line-height:9.4px;width:310px}
  .cutline{left:0;top:753px;width:680px;height:16px}
  .voucher-panel{left:0;top:761px}
  .voucher-offer{left:48px;top:786px;width:150px}
  .voucher-offer .lead{font-weight:600;font-size:12px;line-height:14px;color:var(--ink-teal)}
  .voucher-offer .big{font-weight:700;font-size:52px;line-height:54px;color:#fff}
  .voucher-offer .rabatt{font-weight:700;font-size:15.5px;line-height:17px;color:var(--ink-teal)}
  .voucher-offer .small{margin-top:6px;font-style:italic;font-weight:500;font-size:7.6px;line-height:9.4px;color:var(--ink-teal)}
  .voucher-photo{left:483px;top:761px;width:197px;height:201px;background:linear-gradient(100deg,rgba(255,255,255,0) 0%,#f5e3dc 35%,#eccbbd 100%)}
  .voucher-title{left:213px;top:786px;font-family:"Italiana",serif;font-size:40px;line-height:35px;white-space:nowrap}
  .voucher-title .a{color:var(--pink)}
  .voucher-title .b{color:var(--teal-deep)}
  .voucher-text{left:215px;top:864px;width:350px;font-size:12.3px;line-height:14.5px}
  .voucher-terms{left:215px;top:906px;width:245px;font-style:italic;font-size:7.4px;line-height:9.4px}
</style>
</head>
<body>
<main class="flyer">
  <div class="abs floral-bg" role="img" aria-label="Zarte Blumen-Linienzeichnung im Hintergrund"></div>

  <div class="abs title">Hanni’s</div>
  <div class="abs subtitle">ZEHENGLANZ</div>
  <p class="abs invite">lädt Sie herzlich zur Neueröffnung ein!<br>Ihr neues Fußpflege-Studio in</p>
  <div class="abs location">
    <svg width="16" height="22" viewBox="0 0 16 22"><path d="M8 0C3.6 0 0 3.5 0 7.8 0 13.5 8 22 8 22s8-8.5 8-14.2C16 3.5 12.4 0 8 0zm0 11a3.2 3.2 0 1 1 0-6.4A3.2 3.2 0 0 1 8 11z" fill="#4dbfbf"/></svg>
    <span>Bad Lindenau</span>
  </div>

  <div class="abs brand-mark"><i></i>Hanni’s ZehenGlanz</div>

  <div class="abs intro">
    <div class="greet">Liebe Kundinnen und Kunden,</div>
    <div class="lead">es ist endlich soweit: Mit viel Liebe und Leidenschaft öffnen wir die Türen zu unserem brandneuen Hannis ZehenGlanz in der Lindwurmgasse 47, 8477 Bad Lindenau!</div>
    <div>Tauchen Sie ein in eine Welt, in der Ihre Füße verwöhnt und verschönert werden – ein Ort, an dem Entspannung und Pflege Hand in Hand gehen. Egal, ob Sie intensive Regeneration oder einen frischen Look für Ihre Füße wünschen – bei uns stehen Sie im Mittelpunkt!</div>
  </div>

  <svg class="abs band" width="680" height="170" viewBox="0 0 680 170" role="img" aria-label="Rosafarbenes Wellenband mit dezentem Wellness-Foto">
    <path d="M0 10 C60 -2 120 4 180 18 C270 38 340 36 420 24 C500 14 560 20 640 40 L640 150 C560 140 500 150 420 158 C330 166 250 170 160 158 C100 150 50 150 0 160 Z" fill="#f3a9ca"/>
  </svg>
  <div class="abs why">
    <h2>WARUM ZU UNS?</h2>
    <p>Bei Hannis ZehenGlanz erwarten Sie wohltuende Behandlungen, die Sie nicht nur äußerlich strahlen lassen, sondern Ihnen auch ein tiefes Wohlgefühl schenken. Wir gehen individuell auf Ihre Bedürfnisse ein und gestalten jeden Besuch zu einem besonderen Erlebnis, das Ihnen ein Lächeln ins Gesicht zaubert.</p>
  </div>

  <div class="abs feet-photo" role="img" aria-label="Foto gepflegter Füße mit Orchideenblüte"></div>

  <svg class="abs legs-photo" width="232" height="475" viewBox="0 0 232 475" role="img" aria-label="Fußsohlen-Form mit Foto eines Beins, Handtuch und Bambus in Türkis">
    <defs><linearGradient id="soleTint" x1="0" y1="0" x2="1" y2="1"><stop offset="0" stop-color="#56c3c0"/><stop offset=".6" stop-color="#3db5b3"/><stop offset="1" stop-color="#4ec1c0"/></linearGradient></defs>
    <path d="M0 60 C0 10 40 0 80 0 C140 0 200 30 232 60 L232 473 C205 475 190 450 175 410 C150 340 110 290 75 230 C35 165 0 120 0 60 Z" fill="url(#soleTint)"/>
  </svg>

  <div class="abs quote">”</div>

  <div class="abs booking">
    <h2>Terminvereinbarung</h2>
    <p class="claim">Unser Studio arbeitet mit einem Terminbetrieb, um Ihnen die bestmögliche Betreuung zu gewährleisten.</p>
    <p class="note">Termine sind ausschließlich nach Vereinbarung möglich.<br>Ich freue mich sehr darauf, Ihre Reservierungen</p>
    <p class="date">ab dem &nbsp;|&nbsp; <span class="pink">15.10.2024</span><br>telefonisch unter &nbsp;<span class="phone"><svg width="11" height="11" viewBox="0 0 24 24"><path d="M6.6 10.8a15.1 15.1 0 0 0 6.6 6.6l2.2-2.2a1 1 0 0 1 1-.25 11.4 11.4 0 0 0 3.6.6 1 1 0 0 1 1 1V20a1 1 0 0 1-1 1A17 17 0 0 1 3 4a1 1 0 0 1 1-1h3.5a1 1 0 0 1 1 1c0 1.25.2 2.45.6 3.6a1 1 0 0 1-.25 1z" fill="none" stroke="#ea90ba" stroke-width="2"/></svg>0664/38291647</span></p>
    <p class="sign">Rufen Sie uns an und sichern Sie sich Ihren Wunschtermin!<br>Besuchen Sie uns in unserem gemütlichen und barrierefreien Ambiente und lassen Sie sich von unserer Expertise begeistern. Ihre Füße werden es Ihnen danken! Ich freue mich schon sehr darauf, Sie persönlich bei Hannis ZehenGlanz begrüßen zu dürfen! Herzlichst, Ihre Milena Tarkov</p>
  </div>

  <svg class="abs cutline" width="680" height="16" viewBox="0 0 680 16">
    <line x1="0" y1="8" x2="604" y2="8" stroke="#8a8a8a" stroke-width="1" stroke-dasharray="4 3"/>
    <g stroke="#ea90ba" stroke-width="1.3" fill="none">
      <circle cx="628" cy="4" r="3"/><circle cx="628" cy="12" r="3"/>
      <line x1="625.5" y1="5.5" x2="610" y2="11"/><line x1="625.5" y1="10.5" x2="610" y2="5"/>
    </g>
  </svg>

  <svg class="abs voucher-panel" width="200" height="201" viewBox="0 0 200 201" role="img" aria-label="Türkisfarbenes Gutscheinfeld mit zartem Blumenmuster">
    <path d="M0 0 L170 0 C195 40 195 80 186 120 C178 160 185 185 200 201 L0 201 Z" fill="#79dcdc"/>
  </svg>
  <div class="abs voucher-offer">
    <p class="lead">Profitieren<br>Sie von</p>
    <p class="big">30%</p>
    <p class="rabatt">RABATT AUF<br>ALLE UNSERE</p>
    <p class="small">Behandlungen – ein<br>Geschenk für Sie und<br>Ihre Füße!</p>
  </div>

  <div class="abs voucher-photo" role="img" aria-label="Foto von Füßen auf Zehenspitzen mit Kokosnuss, Handtuch und Orchideen"></div>

  <div class="abs voucher-title"><div class="a">Exklusiver</div><div class="b">Eröffnungsgutschein</div></div>
  <p class="abs voucher-text">Zur Feier unserer Neueröffnung möchten wir Ihnen etwas Besonderes schenken:</p>
  <p class="abs voucher-terms">*Dieser Gutschein ist gültig bis zum 31.12.2024 und einmalig einlösbar. Bitte beachten Sie, dass er nicht mit anderen Aktionen kombinierbar ist.</p>
</main>
</body>
</html>
```